Looking for a web design for event planning. Targeting the Wedding Industry, Corporate Meetings, Special Events, Fundraisers and other Celebratory Events
Home Page - name with pictures of various events- 3 buttons to go to
Wedding ( engagement parties, bridal showers, rehearsal dinners, welcome receptions and wedding receptions page
Corporate Meetings/Fundraisers page
Special Events/Celebratory Events
Updates

Target Market(s)

Brides, Wedding Planners, Corporate Event Planners, Destination Companies, Public

Industry/Entity Type

Event Planning

Contact Information for Business Card

name , phone number and email address
images of party images...wedding cake- balloons-party hat etc

Logo Text

Dana Ruth Korvatch Event Design @ The Bayview Harbor Rowing Society

Number of Pages Required

4 page

Font styles to use
Decorative

Colors

Designer to choose colors to be used in the design.

Requirements
Must have
• Dana Ruth Korvatch Event Design
• @ Bayview Harbor Rowing Society
• 415-555-0193
• drkeventstudio@example-mail.net
• back side of card - Image of Bayview Harbor Rowing Society
Nice to have
• fun and catchy party images
• wedding cake - diamond ring -balloons - party hat- flowers
• would like to see the images in white, gold and silver
Should not have
• photographic pictures

```html
<!DOCTYPE html>
<html lang="en">
<head>
<meta charset="utf-8">
<title>Dana Ruth Korvatch Event</title>
<link href="https://fonts.googleapis.com/css2?family=Great+Vibes&family=Roboto:ital,wght@0,400;0,500;0,700;1,400&display=swap" rel="stylesheet">
<style>
:root{
  --gold:#f6b21a;
  --gold-deep:#e39a0c;
  --ink:#222;
  --muted:#666;
  --white:#fff;
  --footer:#121212;
  --footer-text:#e6e6e6;
  --script:"Great Vibes", cursive;
  --sans:"Roboto", Arial, sans-serif;
}
*{margin:0;padding:0;box-sizing:border-box}
html,body{width:1200px;height:4176px;overflow:hidden;background:var(--white);font-family:var(--sans);color:var(--ink)}
.page{position:relative;width:1200px;height:4176px}
.abs{position:absolute}
.script{font-family:var(--script);font-weight:400}

/* hero */
.hero{left:0;top:0;width:1200px;height:677px;border-top:5px solid var(--gold);
  background:linear-gradient(180deg,#3a2448 0%,#6a3c6e 45%,#4a2a3a 75%,#2c1b22 100%)}
.logo{left:0;width:1200px;top:24px;text-align:center;color:var(--gold)}
.logo .name{font-family:var(--script);font-size:46px;line-height:1}
.logo .sub{font-size:18px;color:var(--white);letter-spacing:2px;margin-top:2px}
.nav{top:140px;left:0;width:1200px;display:flex;justify-content:center;gap:24px;color:var(--white);font-size:15px;font-weight:500}
.nav::after{content:"";position:absolute;left:111px;right:111px;top:-16px;border-top:1px solid rgba(255,255,255,.35)}
.hero-title{left:0;width:1200px;top:330px;text-align:center;color:var(--white)}
.hero-title .big{font-family:var(--script);font-size:120px;line-height:1}
.hero-title .small{font-size:30px;letter-spacing:5px;font-weight:500;margin-top:4px}

/* welcome */
.welcome-h{left:111px;top:755px;font-size:62px;line-height:1.05;color:var(--ink)}
.welcome-p{left:111px;top:912px;width:490px;font-size:15px;line-height:2;color:var(--muted)}
.diamond{width:528px;height:528px;clip-path:polygon(50% 0,100% 50%,50% 100%,0 50%)}
.d-label{color:var(--white);font-weight:700;font-size:34px;text-align:center;width:528px}
.btn-ghost{border:2px solid var(--white);border-radius:24px;color:var(--white);font-size:14px;font-weight:700;padding:10px 22px}
.book-h{right:114px;top:1355px;text-align:right;font-size:66px;line-height:1.15}
.book-p{right:114px;top:1525px;width:510px;text-align:right;font-size:15px;line-height:2;color:var(--muted)}
.btn-gold{left:891px;top:1652px;width:195px;height:50px;border-radius:25px;background:var(--gold);color:var(--white);font-weight:700;font-size:17px;display:flex;align-items:center;justify-content:center;gap:6px}

/* reception */
.reception{left:0;top:1790px;width:1200px;height:540px;background:linear-gradient(180deg,#5a3220 0%,#7a4a30 40%,#a88a78 70%,#d9d3cf 100%)}
.reception-t{left:0;width:1200px;top:1910px;text-align:center;color:var(--white);line-height:1.05}
.reception-t .a{font-size:64px}
.reception-t .b{font-size:84px}

/* gallery */
.gallery-h{left:111px;top:2350px;font-size:66px}
.tile{display:flex;align-items:center;justify-content:center;color:var(--white);font-weight:700;font-size:27px}
.tile.big{background:linear-gradient(160deg,#f4a62a,#e08712 60%,#c8700a);flex-direction:column;gap:22px;font-size:36px}
.tile.grey{background:linear-gradient(160deg,#6b6b6b,#3a3a3a)}
.plus{width:52px;height:52px;border:3px solid var(--white);border-radius:50%;display:flex;align-items:center;justify-content:center;font-size:34px;font-weight:400}

/* testimonials */
.testi{left:0;top:2826px;width:1200px;height:530px;background:linear-gradient(180deg,#efefef,#f7f7f7)}
.testi-h{left:0;width:1200px;top:2895px;text-align:center;font-size:64px}
.avatar{border-radius:50%;background:linear-gradient(160deg,#8a8a8a,#555)}
.avatar.main{border:4px solid var(--gold);background:linear-gradient(160deg,#e8dcd2,#b8a090)}
.arrow{font-size:34px;color:#333}
.client{left:0;width:1200px;top:3150px;text-align:center;font-size:16px;font-weight:700;color:#333}
.client span{font-weight:400;font-style:italic;font-size:14px}
.quote{left:250px;width:700px;top:3192px;text-align:center;font-size:15px;line-height:2;font-style:italic;color:#444}

/* newsletter */
.news{left:0;top:3363px;width:1200px;height:415px;background:linear-gradient(180deg,#f2b51c,#e9a80f 60%,#f0b11a)}
.news-h{left:0;width:1200px;top:3455px;text-align:center;font-size:74px;color:var(--white)}
.news-p{left:250px;width:700px;top:3558px;text-align:center;color:var(--white);font-size:13px;line-height:1.8}
.field{height:42px;background:var(--white);font-size:13px;color:#888;padding:0 12px;display:flex;align-items:center}
.btn-dark{left:718px;top:3633px;width:217px;height:42px;background:#1a1a1a;color:var(--white);font-weight:700;font-size:15px;display:flex;align-items:center;justify-content:center}

/* footer */
.footer{left:0;top:3778px;width:1200px;height:398px;background:var(--footer)}
.f-h{top:3880px;color:var(--white);font-size:17px;font-weight:700}
.f-list{top:3926px;list-style:none;font-size:14px;line-height:26px;color:var(--footer-text)}
.f-list li::before{content:"»";color:var(--white);margin-right:14px}
.contact-row{display:flex;gap:14px;font-size:14px;line-height:1.5;color:var(--footer-text)}
.social{top:3926px;left:877px;display:flex;gap:9px}
.social span{width:34px;height:34px;border:2px solid var(--white);border-radius:50%}
.f-rule{left:111px;width:975px;top:4100px;border-top:1px solid #3a3a3a}
.copy{left:111px;top:4128px;font-size:14px;color:var(--footer-text)}
</style>
</head>
<body>
<div class="page">

  <!-- hero -->
  <div class="abs hero" role="img" aria-label="Photo of a banquet hall with round tables set under purple lighting"></div>
  <div class="abs logo"><div class="name">Dana Ruth</div><div class="sub">KORVATCH EVENT</div></div>
  <nav class="abs nav">
    <span>HOME</span><span>ABOUT US</span><span>WEDDING</span><span>CORPORATE MEETINGS</span><span>FUNDRAISERS</span><span>SPECIAL EVENTS</span><span>CELEBRATORY EVENTS</span><span>CONTACT</span>
  </nav>
  <div class="abs hero-title"><div class="big">Dana Ruth</div><div class="small">KORVATCH EVENT</div></div>

  <!-- welcome -->
  <h1 class="abs welcome-h script">Welcome To Dana Ruth<br>Korvatch Event</h1>
  <p class="abs welcome-p">Lorem ipsum dolor sit amet, consectetur adipiscing sed eiusmod tempor incididunt ut labore et dolore magna aliqua. Ut enim ad minim veniam, sed quia consequuntur magni doloresquis nostrud exercitation ullamco laboris nisi commodo consequat.</p>

  <div class="abs diamond" style="left:669px;top:683px;background:linear-gradient(150deg,#d8d8d8,#7a7a7a 55%,#2e2e2e)" role="img" aria-label="Photo of a bride and groom at a wedding"></div>
  <div class="abs d-label" style="left:669px;top:920px">WEDDING EVENT</div>

  <div class="abs diamond" style="left:335px;top:966px;background:linear-gradient(150deg,#f0b04a,#b86a14 50%,#4a2508)" role="img" aria-label="Photo of a warmly lit banquet room for a corporate meeting"></div>
  <div class="abs d-label" style="left:335px;top:1190px">CORPORATE MEETINGS</div>
  <div class="abs btn-ghost" style="left:521px;top:1255px">BOOK NOW ➜</div>

  <div class="abs diamond" style="left:6px;top:1259px;background:linear-gradient(150deg,#bdbdbd,#6a6a6a 50%,#1e1e1e)" role="img" aria-label="Photo of a dining room set for a special event"></div>
  <div class="abs d-label" style="left:6px;top:1503px">SPECIAL EVENTS</div>

  <h2 class="abs book-h script">Book Your<br>Events With Us!</h2>
  <p class="abs book-p">Nemo enim ipsam voluptatem quia voluptas sit aspernatur aut odit aut consequuntur magni dolores eos qui ratione voluptatem sequi nesciunt. Neque porro quisquam est, qui dolorem ipsum quia dolor sit amet.</p>
  <div class="abs btn-gold">BOOK NOW ➜</div>

  <!-- reception -->
  <div class="abs reception" role="img" aria-label="Photo of a reception hall with string lights and white-clothed tables"></div>
  <svg class="abs" style="left:0;top:2190px" width="1200" height="150" viewBox="0 0 1200 150">
    <path d="M0 150 L0 60 C250 0 500 0 700 40 C900 80 1050 80 1200 60 L1200 150 Z" fill="var(--gold)"/>
    <path d="M0 150 L0 80 C250 20 500 20 700 60 C900 100 1050 100 1200 85 L1200 150 Z" fill="var(--white)"/>
  </svg>
  <div class="abs reception-t script"><div class="a">Reception</div><div class="b">At The Grand Hall</div></div>

  <!-- gallery -->
  <h2 class="abs gallery-h script">Our Gallery</h2>
  <div class="abs tile big" style="left:111px;top:2478px;width:435px;height:339px" role="img" aria-label="Photo of an orange rose wedding cake"><div class="plus">+</div>Wedding Cake</div>
  <div class="abs tile grey" style="left:568px;top:2478px;width:248px;height:158px" role="img" aria-label="Photo of a diamond ring">Diamond Ring</div>
  <div class="abs tile grey" style="left:838px;top:2478px;width:248px;height:158px" role="img" aria-label="Photo of party balloons">Balloons</div>
  <div class="abs tile grey" style="left:568px;top:2659px;width:248px;height:158px" role="img" aria-label="Photo of a decorated party hall">Party Hall</div>
  <div class="abs tile grey" style="left:838px;top:2659px;width:248px;height:158px" role="img" aria-label="Photo of flower arrangements">Flowers</div>

  <!-- testimonials -->
  <div class="abs testi" role="img" aria-label="Faded photo of a banquet room"></div>
  <h2 class="abs testi-h script">What Our Clients Say</h2>
  <div class="abs avatar" style="left:393px;top:3018px;width:72px;height:72px" role="img" aria-label="Client portrait"></div>
  <div class="abs avatar main" style="left:539px;top:2992px;width:124px;height:124px" role="img" aria-label="Client portrait"></div>
  <div class="abs avatar" style="left:735px;top:3018px;width:72px;height:72px" role="img" aria-label="Client portrait"></div>
  <div class="abs arrow" style="left:130px;top:3115px">‹</div>
  <div class="abs arrow" style="left:1050px;top:3115px">›</div>
  <div class="abs client">MAREN HOLLOWAY, <span>Creative Manager</span></div>
  <p class="abs quote">“ Lorem ipsum dolor sit amet, consectetur sit amet adipiscing elit, sed do eiusmod tempor incididunt ut labore et dolore magna aliqua minim veniam quis nostrud exercitation ”</p>

  <!-- newsletter -->
  <div class="abs news" role="img" aria-label="Gold-tinted photo of an event room"></div>
  <h2 class="abs news-h script">Subscribe Newsletter</h2>
  <p class="abs news-p">Lorem ipsum dolor sit amet, consectetur adipiscing elit, sed do eiusmod tempor incididunt ut labore et dolore magna aliqua. Ut enim ad minim veniam quis nostrud exercitation ullamco laboris nisi ut aliquip.</p>
  <div class="abs field" style="left:264px;top:3633px;width:218px">Full Name</div>
  <div class="abs field" style="left:493px;top:3633px;width:214px">Email Address</div>
  <div class="abs btn-dark">SUBSCRIBE NOW!</div>

  <!-- footer -->
  <footer class="abs footer"></footer>
  <div class="abs f-h" style="left:111px">QUICK LINKS</div>
  <ul class="abs f-list" style="left:111px"><li>Home</li><li>About Us</li><li>Wedding</li><li>Corporate Meetings</li><li>Fundraisers</li></ul>
  <div class="abs f-h" style="left:342px">RESOURCES</div>
  <ul class="abs f-list" style="left:342px"><li>Special Events</li><li>Celebratory Events</li><li>Contact us</li><li>Privacy Policy</li><li>Terms &amp; Conditions</li></ul>
  <div class="abs f-h" style="left:585px">CONTACT US</div>
  <div class="abs contact-row" style="left:585px;top:3926px">
    <svg width="16" height="20" viewBox="0 0 16 20"><path d="M8 1a6 6 0 0 0-6 6c0 5 6 12 6 12s6-7 6-12a6 6 0 0 0-6-6z" fill="none" stroke="#e6e6e6" stroke-width="1.5"/><circle cx="8" cy="7" r="2" fill="#e6e6e6"/></svg>
    <span>Old Simple Street, Old City,<br>New State</span>
  </div>
  <div class="abs contact-row" style="left:585px;top:3990px">
    <svg width="16" height="18" viewBox="0 0 16 18"><path d="M3 1l3 3-2 2c1 3 3 5 6 6l2-2 3 3-2 3C7 15 1 9 1 3z" fill="none" stroke="#e6e6e6" stroke-width="1.5"/></svg>
    <span>415-555-0193</span>
  </div>
  <div class="abs contact-row" style="left:585px;top:4032px">
    <svg width="18" height="14" viewBox="0 0 18 14"><rect x="1" y="1" width="16" height="12" fill="none" stroke="#e6e6e6" stroke-width="1.5"/><path d="M1 1l8 7 8-7" fill="none" stroke="#e6e6e6" stroke-width="1.5"/></svg>
    <span>drkeventstudio@example-mail.net</span>
  </div>
  <div class="abs f-h" style="left:877px">SOCIAL MEDIA</div>
  <div class="abs social"><span></span><span></span><span></span><span></span><span></span></div>
  <div class="abs f-rule"></div>
  <div class="abs copy">© Copyright 2018 Dana Ruth Korvatch Event. All Rights Reserved</div>
</div>
</body>
</html>
```